Bold Website Design for Fitness Trainer - No Coding

We are in need of a bold and unique website design for a personal fitness training company, www.TessaRowle.com. We need DESIGN ONLY for three pages. These will be a homepage, a lead capture page, and one internal page with a sidebar. The design will be used for coding a wordpress theme, if that matters for the designer.

Tessa Rowle Fitness Training
2718 E 57th St #193
Austin, TX 78705
512-460-7198
http://www.tessarowle.com

Target Market(s)

18-45 year old male and females making 80k+ a year and looking to get stronger and in shape.

Industry/Entity Type

Fitness

Number of Pages Required

3 page

Font styles to use
Sans Serif

Requirements
Must have
• See attached design specs file.
Nice to have
Should not have
• Boxed layout.
• Dark Background.

```html
<!DOCTYPE html>
<html lang="en">
<head>
<meta charset="utf-8">
<title>Tessa Rowle Fitness Training</title>
<link href="https://fonts.googleapis.com/css2?family=Montserrat:wght@400;600;700;800&family=Open+Sans:ital,wght@0,400;0,600;1,400&display=swap" rel="stylesheet">
<style>
:root{
  --blue:#19a4de;
  --sky:#1bb6ee;
  --purple:#34266f;
  --purple-deep:#261b55;
  --yellow:#ffd21e;
  --yellow-light:#ffe97a;
  --pink:#f0377e;
  --navy:#101a55;
  --ink:#333333;
  --grey:#6d6d6d;
  --card-dark:#3a3a3a;
  --footer:#2a2a2a;
  --footer-deep:#1c1c1c;
  --white:#ffffff;
}
*{box-sizing:border-box;margin:0;padding:0}
html,body{width:1200px;height:3509px;overflow:hidden}
body{font-family:"Open Sans",Arial,sans-serif;color:var(--ink);background:var(--white);position:relative}
.heading{font-family:"Montserrat",Arial,sans-serif;font-weight:700;text-transform:uppercase;letter-spacing:1px}
a{color:inherit;text-decoration:none}

/* top bar */
.topbar{height:54px;background:#fffbe6;display:flex;align-items:center;justify-content:space-between;padding:0 75px;font-family:"Montserrat",sans-serif;font-weight:700;font-size:14px;color:#333}
.topbar .info{display:flex;gap:26px;align-items:center}
.topbar .info span{display:flex;align-items:center;gap:8px}
.topbar .social{display:flex;gap:8px}
.topbar .social i{display:block;width:24px;height:24px;border-radius:4px}

/* header */
.masthead{height:161px;background:radial-gradient(ellipse at 50% 55%,#fff6b8 0%,var(--yellow) 45%,#f7b500 100%);display:flex;align-items:center;justify-content:center;gap:18px}
.brand-mark{width:120px;height:120px;border-radius:50%;background:var(--navy)}
.brand-text{display:flex;flex-direction:column}
.brand-name{font-family:"Montserrat",sans-serif;font-weight:800;font-size:50px;color:var(--navy);line-height:1}
.brand-sub{font-family:"Montserrat",sans-serif;font-weight:800;font-size:20px;color:var(--navy);letter-spacing:2px;text-transform:uppercase;margin-top:4px}

/* nav */
.mainnav{height:52px;background:var(--blue);display:flex;align-items:stretch;padding-left:75px;font-family:"Montserrat",sans-serif;font-weight:700;font-size:16px;color:#fff;text-transform:uppercase}
.mainnav a{display:flex;align-items:center;padding:0 33px}
.mainnav a:first-child{padding-left:33px}
.mainnav .cta{background:var(--pink);margin-left:0}

/* hero */
.hero{height:472px;position:relative;background:linear-gradient(180deg,#1f1f1f,#3a3a3a 50%,#141414);display:flex;flex-direction:column;align-items:center;justify-content:center;color:#fff;text-align:center}
.hero h1{font-size:52px;letter-spacing:3px;font-weight:800}
.hero h2{font-size:32px;letter-spacing:2px;margin-top:4px}
.hero .dots{display:flex;gap:10px;margin-top:30px}
.hero .dots i{width:14px;height:14px;border-radius:50%;background:#fff;opacity:.85}
.hero .dots i:first-child{background:var(--yellow);opacity:1}

/* trial band */
.trial{height:206px;background:linear-gradient(90deg,var(--purple-deep),var(--purple) 50%,var(--purple-deep));display:flex;align-items:center;justify-content:center;gap:34px}
.trial h3{color:#fff;font-size:38px;font-weight:800}
.btn-yellow{background:var(--yellow);color:var(--navy);font-family:"Montserrat",sans-serif;font-weight:800;font-size:20px;padding:18px 20px;text-transform:uppercase;letter-spacing:1px;box-shadow:0 3px 0 #c99c00}

/* services */
.services{height:744px;padding-top:38px;text-align:center}
.section-title{font-size:40px;color:#333;font-weight:700}
.services p.lead{width:1050px;margin:22px auto 0;font-size:13.5px;line-height:26px;color:var(--grey)}
.btn-blue{display:inline-block;background:var(--blue);color:#fff;font-family:"Montserrat",sans-serif;font-weight:700;font-size:19px;padding:12px 24px 18px;margin-top:34px;text-transform:uppercase;letter-spacing:1px;position:relative}
.btn-blue::after{content:"";position:absolute;left:50%;bottom:6px;width:8px;height:8px;border-right:2px solid #fff;border-bottom:2px solid #fff;transform:translateX(-50%) rotate(45deg)}
.cards{display:flex;justify-content:space-between;width:1050px;margin:48px auto 0}
.card{width:330px;height:369px}
.card .photo{height:203px}
.card .label{height:78px;background:var(--sky);color:#fff;display:flex;align-items:center;justify-content:center;font-size:23px;line-height:27px;font-weight:700}
.card .desc{height:88px;background:var(--card-dark);color:#ddd;font-size:12px;line-height:20px;padding:14px 30px}

/* testimonials */
.testimonials{height:418px;background:linear-gradient(180deg,var(--purple),var(--purple-deep));color:#fff;text-align:center;position:relative;padding-top:40px}
.testimonials .section-title{color:#fff}
.testimonials blockquote{width:950px;margin:28px auto 0;font-style:italic;font-size:14.5px;line-height:28px;position:relative}
.testimonials .q{position:absolute;font-family:Georgia,serif;font-size:60px;font-style:normal;top:-20px}
.testimonials .q.l{left:-50px}.testimonials .q.r{right:-50px}
.arrow{position:absolute;top:195px;width:18px;height:18px;border-top:3px solid #fff;border-left:3px solid #fff}
.arrow.prev{left:62px;transform:rotate(-45deg)}
.arrow.next{right:62px;transform:rotate(135deg)}
.avatar{width:72px;height:72px;margin:22px auto 0;border:3px solid #fff;background:#8b6a5a}
.person{font-family:"Montserrat",sans-serif;font-weight:700;font-size:15px;margin-top:16px}
.place{font-size:12px;margin-top:4px}

/* social */
.social-feeds{height:414px;display:flex;justify-content:space-between;padding:38px 75px 0}
.feed{width:512px}
.feed .section-title{text-align:left;font-size:38px;margin-bottom:18px}
.feed-box{border:2px solid #ddd;height:283px;padding:16px 18px}
.grid{display:grid;grid-template-columns:repeat(4,1fr);gap:8px}
.grid i{display:block;height:88px;background:linear-gradient(135deg,#8a7a6e,#c9b8a8)}
.stats{display:flex;gap:36px;margin-top:16px;border-top:1px solid #ddd;padding-top:10px;font-size:11px;color:#666;text-transform:uppercase}
.stats b{display:block;font-size:17px;color:#222;font-family:"Montserrat",sans-serif}
.stats .react{margin-left:auto;display:flex;gap:22px;align-items:center;font-size:15px;color:#333}
.fb-head{display:flex;gap:10px;align-items:center;border-bottom:1px solid #ddd;padding-bottom:12px}
.fb-head .pic{width:40px;height:40px;background:#c9a58f}
.fb-head b{font-size:13px;color:#3b5998}
.fb-head small{display:block;background:#3b5998;color:#fff;font-size:10px;padding:1px 6px;margin-top:4px;width:max-content}
.fb-post{border-left:4px solid #ddd;margin-top:14px;padding:8px 14px;font-size:14px;line-height:22px;color:#333;position:relative;height:160px}
.fb-post .scroll{position:absolute;right:-2px;top:8px;width:6px;height:30px;background:var(--sky)}
.fb-post .likes{color:#3b5998;font-size:12px;margin-top:6px}
.fb-foot{font-size:10px;color:#999;margin-top:10px}

/* blog */
.blog{height:527px;background:var(--sky);padding:60px 75px 0;color:#fff}
.blog .section-title{color:#fff;text-align:left;font-size:38px}
.posts{display:flex;justify-content:space-between;margin-top:28px}
.post{width:330px}
.post .photo{height:185px}
.post h4{font-family:"Montserrat",sans-serif;font-weight:700;font-size:18px;line-height:22px;margin-top:20px;color:var(--navy)}
.post p{font-size:13px;line-height:20px;margin-top:10px}
.post .more{font-family:"Montserrat",sans-serif;font-weight:700;font-size:13px;margin-top:16px;display:block;text-transform:uppercase}

/* signup */
.signup{height:133px;background:var(--yellow);display:flex;align-items:center;justify-content:center;gap:20px}
.signup h3{color:#fff;font-size:38px;font-weight:800}
.signup .field{width:310px;height:52px;background:#fff;font-size:14px;color:#888;display:flex;align-items:center;padding-left:12px}
.btn-navy{background:var(--navy);color:#fff;font-family:"Montserrat",sans-serif;font-weight:800;font-size:18px;padding:15px 18px;text-transform:uppercase;letter-spacing:1px}

/* footer */
.footer{height:250px;background:var(--footer);display:flex;padding:48px 75px 0;color:#bbb}
.footer .col{width:360px}
.footer h5{font-family:"Montserrat",sans-serif;font-weight:700;font-size:27px;color:#fff;text-transform:uppercase;letter-spacing:1px;margin-bottom:18px}
.footer .name{font-family:"Montserrat",sans-serif;font-weight:700;color:var(--sky);font-size:16px;margin-bottom:6px}
.footer p{font-size:12px;line-height:22px;text-transform:uppercase}
.footer p a{color:var(--yellow)}
.footer ul{list-style:none}
.footer li{font-size:12px;line-height:27px;text-transform:uppercase;display:flex;align-items:center;gap:10px}
.footer .res li::before{content:"";width:5px;height:5px;border-top:1px solid #bbb;border-right:1px solid #bbb;transform:rotate(45deg)}
.footer .dot{width:22px;height:22px;border-radius:50%;display:inline-block}
.bottombar{height:78px;background:var(--footer-deep);display:flex;align-items:center;justify-content:space-between;padding:0 75px;font-size:10px;color:#888;text-transform:uppercase}
.bottombar b{font-family:"Montserrat",sans-serif;font-size:24px;color:#fff;font-weight:700}
.bottombar span em{font-style:normal;color:var(--yellow)}
</style>
</head>
<body>

<div class="topbar">
  <div class="info">
    <span><svg width="14" height="14" viewBox="0 0 24 24"><path fill="#e8a800" d="M6.6 10.8a15.1 15.1 0 006.6 6.6l2.2-2.2c.3-.3.7-.4 1-.2 1.1.4 2.3.6 3.6.6.6 0 1 .4 1 1V20c0 .6-.4 1-1 1A17 17 0 013 4c0-.6.4-1 1-1h3.5c.6 0 1 .4 1 1 0 1.3.2 2.5.6 3.6.1.3 0 .7-.2 1z"/></svg>(512) 555-0148</span>
    <span><svg width="12" height="16" viewBox="0 0 12 16"><path fill="#e8a800" d="M6 0a6 6 0 00-6 6c0 4.5 6 10 6 10s6-5.5 6-10a6 6 0 00-6-6zm0 8.5A2.5 2.5 0 116 3.5a2.5 2.5 0 010 5z"/></svg>LAKESHORE ROAD</span>
    <span><svg width="14" height="14" viewBox="0 0 14 14"><rect x="1" y="2" width="12" height="11" fill="none" stroke="#e8a800" stroke-width="2"/><rect x="1" y="2" width="12" height="3" fill="#e8a800"/></svg>APPOINTMENT CALENDAR</span>
  </div>
  <div class="social">
    <i style="background:#3b5998"></i><i style="background:#dd4b39"></i><i style="background:#e62117"></i><i style="background:#cb2027"></i><i style="background:#3f729b"></i>
  </div>
</div>

<header class="masthead">
  <div class="brand-mark"></div>
  <div class="brand-text">
    <span class="brand-name">Tessa Rowle</span>
    <span class="brand-sub">Fitness Training</span>
  </div>
</header>

<nav class="mainnav">
  <a href="#">Home</a><a href="#">Programs</a><a href="#">Meet Your Trainer</a><a href="#">Blog</a><a href="#">Contact Me</a><a href="#" class="cta">Free Session!</a>
</nav>

<section class="hero" role="img" aria-label="Photo of a woman lifting a loaded barbell in a gym">
  <h1 class="heading">Austin's #1 Personal Trainer</h1>
  <h2 class="heading">Workouts Custom Tailored To You</h2>
  <div class="dots"><i></i><i></i><i></i><i></i></div>
</section>

<section class="trial">
  <h3 class="heading">Schedule Your Free Trial</h3>
  <a href="#" class="btn-yellow">Get Started Today</a>
</section>

<section class="services">
  <h2 class="section-title heading">About Our Services</h2>
  <p class="lead">Aliquam molestie, mi et imperdiet euismod, dui purus auctor tellus, et interdum lacus lectus et ante. Sed accumsan sollicitudin sapien, sit amet adipiscing turpis gravida ac. In congue, neque ac lobortis volutpat, libero mauris varius mi, vitae suscipit ipsum ligula vitae risus. Duis aliquam nibh a dui iaculis viverra id a velit. Vivamus egestas risus in magna varius commodo. Sed semper viverra egestas. Etiam pretium porttitor lectus, vel ornare neque porta volutpat. Aenean a nibh eget turpis vehicula tempus ac sed massa. Vestibulum dolor nulla, ultrices ac tincidunt sed, laoreet non est.</p>
  <a href="#" class="btn-blue">Read More</a>
  <div class="cards">
    <article class="card">
      <div class="photo" role="img" aria-label="Photo of a trainer with a client in a gym" style="background:linear-gradient(135deg,#5a5a5a,#b9b0a6)"></div>
      <div class="label heading">1-on-1 Personal<br>Training</div>
      <div class="desc">Duis aliquam nibh a dui iaculis viverra id a velit. Vivamus egestas risus in magna varius commodo.</div>
    </article>
    <article class="card">
      <div class="photo" role="img" aria-label="Photo of a woman using a tablet on an exercise ball" style="background:linear-gradient(135deg,#e8eef2,#9fc7dd)"></div>
      <div class="label heading">Online<br>Coaching</div>
      <div class="desc">Duis aliquam nibh a dui iaculis viverra id a velit. Vivamus egestas risus in magna varius commodo.</div>
    </article>
    <article class="card">
      <div class="photo" role="img" aria-label="Photo of a man deadlifting a heavy barbell" style="background:linear-gradient(135deg,#6e6a66,#3e3a38)"></div>
      <div class="label heading">Strength<br>Programming</div>
      <div class="desc">Duis aliquam nibh a dui iaculis viverra id a velit. Vivamus egestas risus in magna varius commodo.</div>
    </article>
  </div>
</section>

<section class="testimonials">
  <h2 class="section-title heading">Testimonials</h2>
  <blockquote><span class="q l">&ldquo;</span>Aliquam molestie, mi et imperdiet euismod, dui purus auctor tellus, et interdum lacus lectus et ante. Sed accumsan sollicitudin sapien, sit amet adipiscing turpis gravida ac. In congue, neque ac lobortis volutpat, libero mauris varius mi, vitae suscipit ipsum ligula vitae risus. Duis aliquam nibh a dui iaculis viverra id a velit. Vivamus egestas risus in magna varius commodo.<span class="q r">&rdquo;</span></blockquote>
  <i class="arrow prev"></i><i class="arrow next"></i>
  <div class="avatar" role="img" aria-label="Client portrait"></div>
  <div class="person">Name Heading</div>
  <div class="place">Location</div>
</section>

<section class="social-feeds">
  <div class="feed">
    <h2 class="section-title heading">Follow Me On Picstream</h2>
    <div class="feed-box">
      <div class="grid" role="img" aria-label="Grid of eight workout photos">
        <i></i><i></i><i></i><i></i><i></i><i></i><i></i><i></i>
      </div>
      <div class="stats">
        <span><small>Followers</small><b>2972</b></span>
        <span><small>Following</small><b>972</b></span>
        <span><small>Images</small><b>634</b></span>
        <span class="react"><span>&#9675; 19</span><span>&#9825; 173</span></span>
      </div>
    </div>
  </div>
  <div class="feed">
    <h2 class="section-title heading">Like Me On Circlepage</h2>
    <div class="feed-box">
      <div class="fb-head"><div class="pic" role="img" aria-label="Profile photo"></div><div><b>Tessa Rowle</b><small>Like</small></div></div>
      <div class="fb-post">
        <b style="color:#3b5998;font-size:13px">Tessa Rowle</b><br>
        #transformationtuesday! this is a 4 day #transformation! Left is this morning and right is 4 days ago! #leanin #cutting #cardio #weeksout #elite #dieting #nutrition #yeahbuddy
        <div class="likes">47 Likes · 4 Comments</div>
        <i class="scroll"></i>
      </div>
      <div class="fb-foot">Circlepage social plugin</div>
    </div>
  </div>
</section>

<section class="blog">
  <h2 class="section-title heading">Blog Posts</h2>
  <div class="posts">
    <article class="post">
      <div class="photo" role="img" aria-label="Photo of a pepperoni pizza" style="background:linear-gradient(135deg,#c0392b,#e67e22)"></div>
      <h4>Suspendisse lobortis turpis in odio blandit</h4>
      <p>Aliquam molestie, mi et imperdiet euismod, dui purus auctor tellus, et interdum lacus lectus et ante.</p>
      <a href="#" class="more">Read More</a>
    </article>
    <article class="post">
      <div class="photo" role="img" aria-label="Photo of a hand gripping a barbell" style="background:linear-gradient(135deg,#2b2623,#8a7563)"></div>
      <h4>Suspendisse lobortis turpis in odio blandit</h4>
      <p>Aliquam molestie, mi et imperdiet euismod, dui purus auctor tellus, et interdum lacus lectus et ante.</p>
      <a href="#" class="more">Read More</a>
    </article>
    <article class="post">
      <div class="photo" role="img" aria-label="Photo of motivational words printed on paper" style="background:linear-gradient(135deg,#f4f1ea,#b8b2a5)"></div>
      <h4>Suspendisse lobortis turpis in odio blandit</h4>
      <p>Aliquam molestie, mi et imperdiet euismod, dui purus auctor tellus, et interdum lacus lectus et ante.</p>
      <a href="#" class="more">Read More</a>
    </article>
  </div>
</section>

<section class="signup">
  <h3 class="heading">Sign Up Free</h3>
  <div class="field">Enter Email</div>
  <a href="#" class="btn-navy">Get Started Today</a>
</section>

<footer class="footer">
  <div class="col">
    <h5>Contact Address</h5>
    <div class="name">TESSA ROWLE</div>
    <p>4410 Lakeshore<br>Road, Austin TX 78705<br>PH: (512) 555-0148<br>Email: <a href="#">info@tessarowle.com</a></p>
  </div>
  <div class="col">
    <h5>Resources</h5>
    <ul class="res">
      <li>Consectetuer adip</li><li>Song elited diam nonummy</li><li>Nibh euismod tincidunt</li><li>Laoreet dolore magna</li><li>Aliquam erat volut</li>
    </ul>
  </div>
  <div class="col">
    <h5>Connect</h5>
    <ul>
      <li><i class="dot" style="background:#3b5998"></i>Circlepage</li>
      <li><i class="dot" style="background:#dd4b39"></i>Linkplus</li>
      <li><i class="dot" style="background:#e62117"></i>Vidloop</li>
      <li><i class="dot" style="background:#cb2027"></i>Boardly</li>
      <li><i class="dot" style="background:#3f729b"></i>Picstream</li>
    </ul>
  </div>
</footer>

<div class="bottombar">
  <span>Copyright &copy; 2015 <em>Tessa Rowle</em>. All right reserved. Privacy policy and terms of use</span>
  <b>PH: (512) 555-0148</b>
</div>

</body>
</html>
```